Financial Services Consultant needs a business card

We need a business card for a new consulting company based in Melbourne called
"Korvane Metrics". Tagline is GAUGE, GUIDE, CONSERVE
We would like to see business card designs that are in line with the minimal style of the website www.korvane-metrics-example.com
The font I have used on the website is Proxima Nova and would like the same or similar font used on the business card with a minimal design in line with the website Two sided with "KORVANE METRICS" GAUGE, GUIDE, CONSERVE on one side and name, title and contact details on the otther
Updates

Hi All, thanks for your submissions, much appreciated.

I have recently added some colour to my webiste, it is hex #3a7b74 for those that wish to use it
Thanks

Hi all

thanks very much for your design submissions I am very impressed and they are much appreciated.

Interms of general feedback please find below;

Colour: I am trying to stick to a minimal design and colour scheme for my website which is still under construction, up to 3 colours( www.korvane-metrics-example.com) it is currently black and white with a small amount of blue/green but I am open to suggestion/interpretations for a consulting company.

Card: I dont mind if it has rounded edges or straight, I was thinking about using a letterpress card if possible

Detail: the detail on the card will include; Name, Title, Mobile, Personal Email, Business Email,Web,Business Address

Once again thanks for submissions

Industry/Entity Type

Business

```html
<!DOCTYPE html>
<html lang="en">
<head>
<meta charset="utf-8">
<title>Korvane Metrics — Business Card</title>
<link rel="stylesheet" href="https://fonts.googleapis.com/css2?family=Montserrat:wght@300;400;700&display=swap">
<style>
  :root {
    --backdrop: #2e2e2e;
    --card: #ffffff;
    --card-edge: #e4e4e4;
    --ink: #000000;
    --paper-text: #ffffff;
  }
  * { box-sizing: border-box; margin: 0; padding: 0; }
  html, body {
    width: 1128px;
    height: 1200px;
    overflow: hidden;
    background: var(--backdrop);
    font-family: "Montserrat", Arial, sans-serif;
  }
  .canvas { position: relative; width: 1128px; height: 1200px; }

  .card {
    position: absolute;
    left: 197px;
    width: 734px;
    height: 420px;
    background: radial-gradient(ellipse at center, var(--card) 55%, var(--card-edge) 100%);
    overflow: hidden;
  }
  .card--front { top: 159px; }
  .card--back  { top: 616px; }

  .card__frame {
    position: absolute;
    inset: 20px 20px 19px 20px;
    border: 1px solid var(--ink);
  }

  .brand {
    position: absolute;
    left: 0; right: 0;
    top: 154px;
    text-align: center;
    font-weight: 700;
    font-size: 55px;
    line-height: 1;
    letter-spacing: -0.5px;
    color: var(--ink);
    white-space: nowrap;
  }
  .tagline {
    position: absolute;
    left: 165px;
    top: 228px;
    width: 405px;
    height: 30px;
    background: var(--ink);
    color: var(--paper-text);
    font-weight: 400;
    font-size: 18px;
    letter-spacing: 5px;
    line-height: 30px;
    text-align: center;
    white-space: pre;
  }

  .contact-band {
    position: absolute;
    left: 0; right: 0;
    top: 128px;
    height: 168px;
    background: var(--ink);
    color: var(--paper-text);
    text-align: center;
    padding-top: 22px;
  }
  .contact-band__name {
    font-weight: 700;
    font-size: 26px;
    letter-spacing: 2px;
    line-height: 30px;
  }
  .contact-band__line {
    font-weight: 700;
    font-size: 15px;
    letter-spacing: 1px;
    line-height: 23px;
  }
  .contact-band__phone { margin-top: 2px; }
  .contact-band__web {
    font-weight: 300;
    font-size: 19px;
    letter-spacing: 1.5px;
    line-height: 24px;
    white-space: nowrap;
  }
</style>
</head>
<body>
<main class="canvas">
  <section class="card card--front" aria-label="Card front">
    <div class="card__frame"></div>
    <h1 class="brand">KORVANE METRICS</h1>
    <p class="tagline">GAUGE,  GUIDE,  CONSERVE</p>
  </section>

  <section class="card card--back" aria-label="Card back">
    <div class="card__frame"></div>
    <div class="contact-band">
      <p class="contact-band__name">KORVANE METRICS</p>
      <p class="contact-band__line contact-band__phone">0800 555 0142</p>
      <p class="contact-band__line">Larrow Street Carrowby</p>
      <p class="contact-band__line">Carrowby VIC 3999, Australia</p>
      <p class="contact-band__web">http://www.korvane-metrics-example.com</p>
    </div>
  </section>
</main>
</body>
</html>
```